Breezeway Comfort business cards design

Need a business card design for a Heating and Air Conditioning business. I need these items included.
Business name: Breezeway Comfort
Owner: Marcus Holloway
License # 2748519
Phone number # 555-382-4067
Email: breezewaycomfortair@mailnest.example
Sales
Service
Installation
Maintenance

Heating and Air Conditioning

Requirements
Must have
• Company name , license number , phone number , email

```html
<!DOCTYPE html>
<html lang="en">
<head>
<meta charset="utf-8">
<title>Breezeway Comfort – Business Cards</title>
<link href="https://fonts.googleapis.com/css2?family=Roboto:wght@400;700;900&display=swap" rel="stylesheet">
<style>
  :root {
    --stage: #1d1f22;
    --royal: #0637a8;
    --royal-deep: #05319a;
    --paper: #f3f3f3;
    --orange: #f0782a;
    --amber: #f4a02b;
    --magenta: #e0196d;
    --ink-soft: #4a4a4a;
  }
  * { box-sizing: border-box; margin: 0; padding: 0; }
  html, body { width: 1200px; height: 840px; overflow: hidden; }
  body {
    background: var(--stage);
    font-family: "Roboto", Arial, sans-serif;
    position: relative;
  }
  .card {
    position: absolute;
    width: 540px;
    height: 310px;
    border-radius: 26px;
    overflow: hidden;
    box-shadow: 0 4px 0 -1px var(--orange), 3px 4px 0 -1px var(--magenta), 0 18px 30px rgba(0,0,0,.45);
  }
  .card--front { left: 70px; top: 90px; background: linear-gradient(160deg, var(--royal), var(--royal-deep)); }
  .card--back { left: 590px; top: 440px; background: var(--paper); }

  .brand {
    position: absolute;
    display: flex;
    align-items: center;
    gap: 12px;
    font-weight: 900;
    font-size: 34px;
    letter-spacing: .5px;
    text-transform: uppercase;
    white-space: nowrap;
  }
  .brand__dot { width: 26px; height: 26px; border-radius: 50%; background: var(--orange); flex: none; }
  .card--front .brand { left: 70px; top: 92px; color: #ffffff; }
  .card--back .brand { left: 80px; top: 58px; color: var(--royal); }

  .services {
    position: absolute;
    left: 0; right: 0; top: 190px;
    text-align: center;
    color: #ffffff;
    font-size: 19px;
    line-height: 30px;
  }
  .services__item::before {
    content: "";
    display: inline-block;
    width: 8px; height: 8px;
    border-radius: 50%;
    background: var(--orange);
    margin: 0 6px 3px 10px;
    vertical-align: middle;
  }

  .owner { position: absolute; left: 16px; top: 160px; width: 196px; text-align: right; }
  .owner__name { color: var(--royal); font-weight: 700; font-size: 20px; text-transform: uppercase; white-space: nowrap; }
  .owner__role { color: var(--orange); font-size: 17px; margin-top: 2px; }
  .divider { position: absolute; left: 226px; top: 155px; width: 1px; height: 62px; background: var(--ink-soft); }
  .contacts { position: absolute; left: 240px; top: 160px; color: var(--ink-soft); font-size: 15px; line-height: 26px; }
  .contacts__row { display: flex; align-items: center; gap: 6px; white-space: nowrap; }
  .contacts__row svg { width: 14px; height: 14px; flex: none; }
  .contacts__row--email { font-size: 13px; }

  .license-tab { position: absolute; right: 0; bottom: 0; width: 300px; height: 56px; }
  .license-tab__text {
    position: absolute; right: 40px; bottom: 14px;
    color: #ffffff; font-size: 17px;
  }
</style>
</head>
<body>
  <section class="card card--front" aria-label="Card front">
    <div class="brand"><span class="brand__dot"></span>Breezeway Comfort</div>
    <div class="services">
      <div><span class="services__item">Sales</span> <span class="services__item">Service</span></div>
      <div><span class="services__item">Installation</span> <span class="services__item">Maintenance</span></div>
    </div>
  </section>

  <section class="card card--back" aria-label="Card back">
    <div class="brand"><span class="brand__dot"></span>Breezeway Comfort</div>
    <div class="owner">
      <div class="owner__name">Marcus Holloway</div>
      <div class="owner__role">Owner</div>
    </div>
    <div class="divider"></div>
    <div class="contacts">
      <div class="contacts__row">
        <svg viewBox="0 0 24 24"><path fill="#f0782a" d="M6.6 10.8a15 15 0 0 0 6.6 6.6l2.2-2.2a1 1 0 0 1 1-.25 11.4 11.4 0 0 0 3.6.57 1 1 0 0 1 1 1V20a1 1 0 0 1-1 1A17 17 0 0 1 3 4a1 1 0 0 1 1-1h3.5a1 1 0 0 1 1 1c0 1.25.2 2.45.57 3.570a1 1 0 0 1-.25 1z"/></svg>
        555-382-4067
      </div>
      <div class="contacts__row contacts__row--email">
        <svg viewBox="0 0 24 24"><path fill="#f0782a" d="M3 5h18a1 1 0 0 1 1 1v12a1 1 0 0 1-1 1H3a1 1 0 0 1-1-1V6a1 1 0 0 1 1-1zm9 8 8-5.5V7l-8 5.5L4 7v.5z"/></svg>
        breezewaycomfortair@mailnest.example
      </div>
    </div>
    <svg class="license-tab" viewBox="0 0 300 56" preserveAspectRatio="none" aria-hidden="true">
      <defs>
        <linearGradient id="tabFill" x1="0" x2="1" y1="0" y2="0">
          <stop offset="0" stop-color="#e8394f"/>
          <stop offset="1" stop-color="#d9146e"/>
        </linearGradient>
      </defs>
      <path d="M0 56 L14 18 Q20 4 36 4 L300 4 L300 56 Z" fill="url(#tabFill)"/>
    </svg>
    <div class="license-tab__text">License # 2748519</div>
  </section>
</body>
</html>
```